Corvexa_how it works_step by step_icons

Looking to create 4 icons that represent the how it works for Corvexa
Steps:
JOIN
Sign up for FREE and qualify for Corvexa Loan Perks.
SHOP
Shop our curated boutique of online stores and earn towards an interest free loan with every purchase.
FORWARD
Once you have completed your purchase with one of our online stores, forward your email receipt to receipt@corvexa-mail.com to verify your purchase.
EARN
Loan amounts accrue with every qualified purchase and can be redeemed at any time. Choose a loan option that's right for you with 3,6, or 9 month terms.
Target Market(s)
Online millennial shoppers looking to purchase fashion, travel, and entertainment.
Industry/Entity Type
Loan
Colors
Designer to choose colors to be used in the design.
Look and feel
Each slider illustrates characteristics of the customer's brand and the style your logo design should communicate.

```html
<!DOCTYPE html>
<html lang="en">
<head>
<meta charset="utf-8">
<title>Corvexa – How It Works</title>
<link rel="stylesheet" href="https://fonts.googleapis.com/css2?family=Open+Sans:wght@400;700&display=swap">
<style>
  :root {
    --brand-blue: #3c54a0;
    --brand-blue-soft: #3e57a3;
    --paper: #ffffff;
    --ink: #111111;
  }
  * { margin: 0; padding: 0; box-sizing: border-box; }
  html, body { width: 1200px; height: 1000px; overflow: hidden; background: var(--paper); }
  .canvas {
    position: relative;
    width: 1200px;
    height: 1000px;
    font-family: "Open Sans", sans-serif;
    background: var(--paper);
  }
  .top-band {
    position: absolute; left: 0; top: 0;
    width: 1200px; height: 143px;
    background: var(--brand-blue);
  }
  .brand-plate {
    position: absolute; left: 372px; top: 15px;
    width: 376px; height: 120px;
    background: var(--brand-blue-soft);
  }
  .brand-name {
    position: absolute; left: 372px; top: 15px;
    width: 376px; height: 120px;
    display: flex; align-items: center; justify-content: center;
    color: var(--paper);
    font-weight: 700;
    font-size: 62px;
    letter-spacing: 2px;
    padding-right: 30px;
  }
  .steps-main {
    position: absolute; left: 0; top: 400px;
    width: 1200px;
  }
  .step {
    position: absolute;
    width: 260px;
    text-align: center;
  }
  .step-icon { display: block; margin: 0 auto; }
  .steps-main .step { top: 0; margin-left: -130px; }
  .steps-main .step-icon { width: 148px; height: 148px; --disc: var(--brand-blue); --mark: var(--paper); }
  .steps-main .step-label {
    margin-top: 14px;
    font-size: 36px; font-weight: 400;
    color: var(--ink);
    line-height: 48px;
    letter-spacing: 0.5px;
  }
  .bottom-band {
    position: absolute; left: 0; top: 857px;
    width: 1200px; height: 143px;
    background: var(--brand-blue);
  }
  .steps-mini .step { top: 24px; margin-left: -70px; width: 140px; }
  .steps-mini .step-icon { width: 74px; height: 74px; --disc: var(--paper); --mark: var(--brand-blue); }
  .steps-mini .step-label {
    margin-top: 4px;
    font-size: 17px;
    color: var(--paper);
    line-height: 24px;
  }
  .disc { fill: var(--disc); }
  .mark { fill: none; stroke: var(--mark); stroke-width: 3; stroke-linecap: round; stroke-linejoin: round; }
  .mark-fill { fill: var(--mark); }
  .dollar { fill: var(--mark); font-family: "Open Sans", sans-serif; font-size: 92px; font-weight: 400; }
</style>
</head>
<body>
<svg width="0" height="0" style="position:absolute" aria-hidden="true">
  <defs>
    <clipPath id="disc-clip"><circle cx="74" cy="74" r="74"/></clipPath>
    <symbol id="icon-join" viewBox="0 0 148 148">
      <circle class="disc" cx="74" cy="74" r="74"/>
      <g clip-path="url(#disc-clip)">
        <path class="mark" d="M76 -2 V28 A8 8 0 1 0 76 42 V72 L78 106 A8 8 0 1 1 79 120 L81 150"/>
        <path class="mark" d="M-2 74 L36 72 A8 8 0 1 0 50 71 L76 72 L100 70 A8 8 0 1 1 114 69 L150 66"/>
      </g>
    </symbol>
    <symbol id="icon-shop" viewBox="0 0 148 148">
      <circle class="disc" cx="74" cy="74" r="74"/>
      <g clip-path="url(#disc-clip)">
        <path class="mark" d="M12 30 L22 52 L34 112 L120 112"/>
        <path class="mark" d="M22 52 H134 L126 105 H34"/>
        <path class="mark" d="M26 70 H131 M30 88 H128"/>
        <path class="mark" d="M50 52 L56 105 M76 52 L78 105 M104 52 L100 105"/>
        <circle class="mark-fill" cx="47" cy="122" r="5"/>
        <circle class="mark-fill" cx="100" cy="122" r="5"/>
      </g>
    </symbol>
    <symbol id="icon-forward" viewBox="0 0 148 148">
      <circle class="disc" cx="74" cy="74" r="74"/>
      <g clip-path="url(#disc-clip)">
        <path class="mark" d="M8 28 L50 74 L12 122"/>
        <path class="mark" d="M34 28 L76 74 L36 122"/>
        <path class="mark" d="M58 28 L100 74 L60 122"/>
        <path class="mark" d="M82 28 L124 74 L84 122"/>
      </g>
    </symbol>
    <symbol id="icon-earn" viewBox="0 0 148 148">
      <circle class="disc" cx="74" cy="74" r="74"/>
      <text class="dollar" x="74" y="106" text-anchor="middle">$</text>
    </symbol>
  </defs>
</svg>

<main class="canvas">
  <header class="top-band">
    <div class="brand-plate"></div>
    <div class="brand-name">Corvexa</div>
  </header>

  <section class="steps-main">
    <div class="step" style="left:144px">
      <svg class="step-icon" viewBox="0 0 148 148" aria-hidden="true"><use href="#icon-join"/></svg>
      <div class="step-label">JOIN</div>
    </div>
    <div class="step" style="left:448px">
      <svg class="step-icon" viewBox="0 0 148 148" aria-hidden="true"><use href="#icon-shop"/></svg>
      <div class="step-label">SHOP</div>
    </div>
    <div class="step" style="left:752px">
      <svg class="step-icon" viewBox="0 0 148 148" aria-hidden="true"><use href="#icon-forward"/></svg>
      <div class="step-label">FORWARD</div>
    </div>
    <div class="step" style="left:1056px">
      <svg class="step-icon" viewBox="0 0 148 148" aria-hidden="true"><use href="#icon-earn"/></svg>
      <div class="step-label">EARN</div>
    </div>
  </section>

  <footer class="bottom-band steps-mini">
    <div class="step" style="left:370px">
      <svg class="step-icon" viewBox="0 0 148 148" aria-hidden="true"><use href="#icon-join"/></svg>
      <div class="step-label">JOIN</div>
    </div>
    <div class="step" style="left:523px">
      <svg class="step-icon" viewBox="0 0 148 148" aria-hidden="true"><use href="#icon-shop"/></svg>
      <div class="step-label">SHOP</div>
    </div>
    <div class="step" style="left:676px">
      <svg class="step-icon" viewBox="0 0 148 148" aria-hidden="true"><use href="#icon-forward"/></svg>
      <div class="step-label">FORWARD</div>
    </div>
    <div class="step" style="left:830px">
      <svg class="step-icon" viewBox="0 0 148 148" aria-hidden="true"><use href="#icon-earn"/></svg>
      <div class="step-label">EARN</div>
    </div>
  </footer>
</main>
</body>
</html>
```